Velvet Harbor for sale at the 2019 Tandor Crest Mare Auction on 30 May 2019

I am selling my broodmare at the 2019 Tandor Crest Mare auction on 30 May 2019. I need a flyer to hand out to potential buyers. I have included the required information in the attached word document. I can provide more images if required. I am thinking that a DL double sided or an A5 will suit best. I'm happy to provide more information as required.

Target Market(s)

Race horse breeders, people who buy broodmares.

Font styles to use
Serif
Sans Serif
Script

Colors

Designer to choose colors to be used in the design.

Requirements
Must have
• All of the content provided in the attached brief, however it is not necessary to have the words exactly as per the brief. The brief is for information purposes.
Nice to have
• Innovation...

```html
<!DOCTYPE html>
<html lang="en">
<head>
<meta charset="utf-8">
<title>Velvet Harbor – Broodmare Flyer</title>
<link rel="stylesheet" href="https://fonts.googleapis.com/css2?family=Montserrat:wght@400;800&family=Source+Sans+3:wght@400;600;700&family=Oswald:wght@500;600&display=swap">
<style>
:root{
  --bg:#8a8a8a;
  --red:#c8161e;
  --red-dark:#a80f16;
  --black:#0b0b0b;
  --white:#ffffff;
  --ink:#1a1a1a;
  --grass:#4f9a2c;
  --grass-light:#7cc447;
  --sky:#cfe3f2;
}
*{box-sizing:border-box;margin:0;padding:0}
html,body{width:1200px;height:1200px;overflow:hidden}
body{background:var(--bg);position:relative;font-family:"Source Sans 3",sans-serif;color:var(--ink)}
.page{position:absolute;top:296px;width:425px;height:608px;background:var(--white);overflow:hidden}
.page--front{left:150px}
.page--back{left:626px}

.hero-photo{position:absolute;left:0;top:0;width:425px;height:240px;
  background:linear-gradient(180deg,#3c6a22 0%,#5c8f34 35%,#6e5a3c 60%,#5f9a35 80%,var(--grass-light) 100%)}
.title-band{position:absolute;left:0;top:240px;width:425px;height:59px;background:var(--black);text-align:center;color:var(--white)}
.title-band h1{font-family:"Montserrat",sans-serif;font-weight:800;font-size:31px;color:var(--red);line-height:1;margin-top:5px;letter-spacing:.5px}
.title-band p{font-family:"Montserrat",sans-serif;font-size:18px;line-height:1.1;margin-top:1px}

.facts{position:absolute;left:10px;top:299px;width:188px;height:309px;
  background:linear-gradient(90deg,var(--red-dark) 0%,var(--red) 60%,#d23a3f 100%);
  color:var(--white);padding:5px 8px 0 11px}
.facts dt{display:inline;font-weight:700;font-size:15px}
.facts dd{display:inline;font-size:12.5px}
.facts .row{line-height:1.25;margin-bottom:4px}
.facts .note{font-size:10.3px;font-weight:600;line-height:1.3;text-align:justify;margin-top:6px}

.shot{position:absolute;border:3px solid var(--red);background:var(--red)}
.shot .photo{width:100%;background:linear-gradient(180deg,var(--sky) 0%,#3f6e38 30%,#2a2a2a 50%,var(--grass) 62%,var(--grass-light) 100%)}
.shot .caption{color:var(--white);font-weight:700;text-align:center;font-size:14px;line-height:1.1;display:flex;align-items:center;justify-content:center}
.race-info{position:absolute;text-align:center;font-size:9.6px;font-weight:600;line-height:1.25}

.contact{position:absolute;left:198px;top:530px;width:227px;height:62px;background:var(--black);text-align:center;color:var(--white)}
.contact .call{font-family:"Oswald",sans-serif;font-weight:600;font-size:20px;margin-top:7px;line-height:1.2}
.contact .call span{color:var(--red)}
.contact .web{font-size:10px;letter-spacing:1px;margin-top:3px;display:flex;align-items:center;justify-content:center;gap:3px}
.contact .web i{width:6px;height:6px;border-radius:50%;background:var(--red);display:inline-block}

.footer-bar{position:absolute;left:0;top:592px;width:425px;height:16px;background:var(--black)}
</style>
</head>
<body>

<section class="page page--front">
  <div class="hero-photo" role="img" aria-label="Field of racehorses and jockeys rounding a turn on a grass track"></div>
  <header class="title-band">
    <h1>VELVET HARBOR</h1>
    <p>(by Sparkwell, out of Bonavista)</p>
  </header>

  <dl class="facts">
    <div class="row"><dt>Lot number:</dt> <dd>1414</dd></div>
    <div class="row"><dt>Stable:</dt> <dd>QC 6</dd></div>
    <div class="row"><dt>Sale date:</dt> <dd>30 May 2019</dd></div>
    <div class="row"><dt>Sale:</dt> <dd>2019 Tandor Crest Mare Auction</dd></div>
    <div class="row"><dt>Race record:</dt> <dd>7 wins, 2 seconds, 2 thirds (27-7:2:2), $205,400 prizemoney</dd></div>
    <p class="note">In foal to Far Meadow, sire of: Stellar Drive (winner of the Group 3 Palo Verde Stakes by 7.5L), Burrow Down (winner of the Group 2 Karranya Plate), Harrier Gale (winner of the Tandor Crest Clockwise Classic), Swift Arrow, Coupe Ray plus more...</p>
  </dl>

  <figure class="shot" style="left:212px;top:306px;width:191px;height:173px">
    <div class="photo" role="img" aria-label="Velvet Harbor crossing the finish line ahead of the big screen" style="height:143px"></div>
    <figcaption class="caption" style="height:24px">Velvet Harbor wins by 3.5L</figcaption>
  </figure>
  <p class="race-info" style="left:212px;top:482px;width:191px;font-size:10.3px">Class 6 Handicap – 1400m<br>Riverbend Racing Club (Heron Park),<br>21 January 2017</p>

  <div class="contact">
    <p class="call"><span>CALL US :</span> 1234567890</p>
    <p class="web"><i></i>www.VelvetHarbor</p>
  </div>
</section>

<section class="page page--back">
  <figure class="shot" style="left:24px;top:22px;width:184px;height:184px">
    <div class="photo" role="img" aria-label="Velvet Harbor winning on the home straight" style="height:153px"></div>
    <figcaption class="caption" style="height:25px">Velvet Harbor wins by 2.8L</figcaption>
  </figure>
  <p class="race-info" style="left:24px;top:209px;width:184px">No More Than One Metro<br>Win Handicap – 1400m<br><span style="display:block;margin-top:5px">Riverbend Racing Club (Heron Park),<br>10 December 2016</span></p>

  <figure class="shot" style="left:216px;top:22px;width:185px;height:197px">
    <div class="photo" role="img" aria-label="Velvet Harbor leading the field to the finish" style="height:154px"></div>
    <figcaption class="caption" style="height:37px;font-size:14px">Velvet Harbor beats<br>Pirouetta by 1.3L</figcaption>
  </figure>
  <p class="race-info" style="left:216px;top:222px;width:185px">Class 6 Plate – 1300m<br>Riverbend Racing Club (Heron Park),<br>29 April 2017</p>

  <figure class="shot" style="left:24px;top:271px;width:377px;height:125px">
    <div class="photo" role="img" aria-label="Velvet Harbor racing clear past the grandstand" style="height:95px"></div>
    <figcaption class="caption" style="height:24px">Velvet Harbor wins by 2.3L</figcaption>
  </figure>
  <p class="race-info" style="left:24px;top:401px;width:377px">Class 4 Handicap – 1400m<br>Riverbend Racing Club (Dunmore), 23 November 2016</p>

  <figure class="shot" style="left:22px;top:432px;width:377px;height:125px">
    <div class="photo" role="img" aria-label="Velvet Harbor winning her debut race" style="height:95px"></div>
    <figcaption class="caption" style="height:24px">Velvet Harbor wins on debut at the Suncrest Coast!</figcaption>
  </figure>
  <p class="race-info" style="left:22px;top:561px;width:377px">Maiden – 1000m<br>Suncrest Coast Turf Club, 23 October 2015</p>

  <div class="footer-bar"></div>
</section>

</body>
</html>
```